Brochure Design

I would like to have this brochure design for a approval with the Morvale chamber of commerce . It's a training program for people in Kenya Africa and the gov will pay for the training program. What ever you think would be better let me know. The letters in red are items that are free so I wanted that to stand out. I need to add the logo in the attachment added to the other logos on the front page.

Reason: I'm still looking for the right design and i'm looking to make a quick decision.

```html
<!DOCTYPE html>
<html lang="en">
<head>
<meta charset="utf-8">
<title>Kestrel Vantage Partners — Training Program Outline</title>
<link href="https://fonts.googleapis.com/css2?family=Arimo:wght@400;700&family=Roboto:wght@300;400&display=swap" rel="stylesheet">
<style>
  :root{
    --backdrop:#e4e2df;
    --paper:#ffffff;
    --paper-shade:#d9dadb;
    --panel-grey:#c3c4c6;
    --orange:#f2a83b;
    --orange-deep:#e99a2a;
    --charcoal:#4a4d52;
    --ink:#2b2b2b;
    --heading:#5a5a5a;
    --rule:#f0b45a;
  }
  *{box-sizing:border-box;margin:0;padding:0}
  html,body{width:1200px;height:900px;overflow:hidden}
  body{background:var(--backdrop);font-family:"Arimo",Arial,sans-serif;color:var(--ink);position:relative}

  .spread{position:absolute;left:38px;top:55px;width:1127px;height:797px;display:flex;box-shadow:0 2px 10px rgba(0,0,0,.18)}
  .page{position:relative;height:100%;overflow:hidden}
  .page--left{width:565px;background:linear-gradient(90deg,var(--paper-shade) 0%,#f4f4f4 12%,var(--paper) 40%,var(--paper) 88%,#ececec 100%)}
  .page--right{width:562px;background:linear-gradient(90deg,#c9cacc 0%,#e6e6e7 10%,#f6f6f6 30%,var(--paper) 60%)}

  .abs{position:absolute}
  .tab{background:linear-gradient(90deg,var(--orange-deep),var(--orange));border-top-right-radius:18px}
  .photo{position:absolute}
  .section-title{font-family:"Roboto",Helvetica,sans-serif;font-weight:300;color:var(--heading);font-size:21px;line-height:22px;letter-spacing:.3px;text-transform:uppercase}
  .body-text{font-size:11.2px;line-height:13.4px;color:var(--ink);hyphens:auto;-webkit-hyphens:auto}
  .justify{text-align:justify}

  .item-title{font-size:10.8px;font-weight:700;color:#555;padding-bottom:3px;border-bottom:1px solid var(--rule);margin-bottom:5px}
  .item{margin-bottom:5px}
  .item-photo{float:left;width:112px;height:86px;margin:0 5px 3px 1px;background:linear-gradient(180deg,#9fb5c9 0%,#7f8d7c 25%,#5f8b3d 55%,#7aa64a 100%)}

  .skill-title{font-family:"Roboto",Helvetica,sans-serif;font-weight:300;font-size:15px;color:#444;text-transform:uppercase;line-height:16px}

  .footer{position:absolute;bottom:0;height:46px;border-left:2px solid var(--orange);font-size:9.5px;color:#555;padding-top:14px}
  .footer b{font-weight:400;color:#333}

  .label-dark{background:var(--charcoal);color:var(--orange);font-family:"Roboto",Helvetica,sans-serif;font-size:15px;padding:1px 0 0 6px;letter-spacing:.3px}
  .sub-head{font-size:12px;font-weight:700;color:#555}

  .info-panel{position:absolute;left:285px;top:0;width:277px;height:293px;background:var(--panel-grey);border-bottom-left-radius:40px}
  .info-tab{position:absolute;left:27px;width:147px;background:var(--orange);border-top-right-radius:12px;color:#fff;font-size:10.5px;font-weight:700;line-height:11px;padding:5px 9px}
  .info-bar{position:absolute;left:27px;width:250px;height:19px;background:var(--charcoal);color:#f6d9a6;font-size:10.5px;font-weight:700;padding:3px 9px}
</style>
</head>
<body>
<main class="spread">

  <section class="page page--left">
    <div class="abs tab" style="left:52px;top:52px;width:223px;height:43px"></div>
    <div class="photo" role="img" aria-label="Landscaped residential garden with lawn, shrubs and a low house" style="left:52px;top:102px;width:223px;height:122px;background:linear-gradient(180deg,#a9c2dc 0%,#c8d6e2 28%,#6f8a4a 45%,#4e7a2c 70%,#8a6a4a 100%)"></div>
    <h2 class="section-title abs" style="left:287px;top:162px">Commercial<br>&amp; Residential<br>Landscaping</h2>

    <p class="body-text abs" style="left:52px;top:252px;width:455px">In order to ensure the exterior of buildings and homes are kept beautiful and free of fire hazards, it is important to have the proper equipment, training, and knowledge. &nbsp;Kestrel Vantage Partners can provide equipment and training which will prove to be extremely useful in daily life.</p>
    <p class="body-text abs" style="left:52px;top:311px;width:458px">Some of the equipment to be utilized and potentially purchased is as follows:</p>

    <div class="abs" style="left:52px;top:337px;width:223px">
      <div class="item">
        <h3 class="item-title">Weed-Whacker</h3>
        <div class="item-photo" role="img" aria-label="Weed-whacker and mower on a striped lawn"></div>
        <p class="body-text">A tool which uses a flexible monofilament line instead of a blade for cutting grass and other plants which are near objects or hard to reach places including steep or irregular terrain. &nbsp;It typically has a long shaft with a handle and a cutting head at the end of the shaft.</p>
      </div>
      <div class="item" style="margin-top:4px">
        <h3 class="item-title">Lawn Mower</h3>
        <p class="body-text">Used to trim grass and can be a hand-pushed object or a ride on style.</p>
      </div>
    </div>

    <div class="abs" style="left:287px;top:337px;width:223px">
      <div class="item"><h3 class="item-title">Brush Cutter</h3><p class="body-text">A heavy duty tool that can clear saplings or dense under growth with ease.</p></div>
      <div class="item"><h3 class="item-title">Chainsaw</h3><p class="body-text">A handheld, gas powered saw which has the power to cut large trees.</p></div>
      <div class="item"><h3 class="item-title">Blower</h3><p class="body-text">A tool which blows air with extreme force in order to push debris from one area to another.</p></div>
      <div class="item"><h3 class="item-title">Hedge Trimmer</h3><p class="body-text">Either electric or gas powered versions exist, and are used to efficiently trim bushes and hedges for a manicured look.</p></div>
    </div>

    <div class="abs tab" style="left:52px;top:593px;width:223px;height:22px;border-top-right-radius:12px;font-size:10px;font-weight:700;color:#3a3a3a;padding:5px 8px">Other Skills</div>

    <div class="abs" style="left:53px;top:629px;width:218px">
      <h3 class="skill-title">Sprinklers</h3>
      <p class="body-text">Learn how to dig proper ditches for efficient drainage, lay sprinkler pipes, and sprinkler head placement for most effective water coverage. &nbsp;Also understand electric control panels and how to program and operate.</p>
    </div>
    <div class="abs" style="left:287px;top:629px;width:223px">
      <h3 class="skill-title">Design Techniques</h3>
      <p class="body-text">Learn how to beautify grounds through design and strategic placement of specific plants and hardscape items.</p>
    </div>

    <footer class="footer" style="left:32px">
      <span style="position:absolute;left:-16px;top:14px;font-size:11px">10</span>
      <span style="padding-left:6px"><b>KESTREL VANTAGE PARTNERS</b> TRAINING PROGRAM OUTLINE</span>
    </footer>
  </section>

  <section class="page page--right">
    <div class="info-panel">
      <div class="info-tab" style="top:157px">Class Dates (2015)</div>
      <div class="info-bar" style="top:188px">May 20-30</div>
      <div class="info-tab" style="top:225px">Final Registration and Deposit Due</div>
      <div class="info-bar" style="top:256px">December 31, 2015</div>
    </div>

    <div class="abs label-dark" style="left:51px;top:94px;width:156px;height:19px;line-height:17px">EQUIPMENT</div>
    <p class="body-text abs" style="left:51px;top:121px;width:224px">This training will provide participants with a weedwhacker and a blower so that they may have the tools to start a business right away upon completion of the training.</p>

    <h3 class="sub-head abs" style="left:51px;top:212px">Training Time and Cost</h3>
    <p class="body-text abs" style="left:51px;top:229px;width:224px">Training program can be customized for 3 days. &nbsp;Cost: $2100 per person. &nbsp;Minimum class size of 20 required. &nbsp;Classes to be provided in Nairobi, Kenya.</p>

    <div class="abs tab" style="left:51px;top:409px;width:374px;height:41px"></div>
    <div class="photo" role="img" aria-label="Indoor fish farming tanks under warm lights" style="left:285px;top:458px;width:222px;height:109px;background:linear-gradient(180deg,#6b6a5c 0%,#c9c19a 18%,#55584d 40%,#6a5434 70%,#3f3a2a 100%)"></div>
    <h2 class="section-title abs" style="left:51px;top:523px">Commercial<br>Fish Farming</h2>

    <p class="body-text justify abs" style="left:51px;top:584px;width:223px">Commercial fish farming can be accomplished on a large scale inside of specialized enclosures which can be installed in any location in the world. &nbsp;The term “aquaculture” is used to describe the process by which fish are grown and harvested in these farms. &nbsp;The result is a business that provides a much needed commodity, jobs for local residents, and profits for the business owner.</p>
    <p class="body-text justify abs" style="left:285px;top:584px;width:223px">Kestrel Vantage Partners provides access to the technology and equipment as well as training for potential business operators and employees. &nbsp;This ensures that individuals have the knowledge and experience required to successfully run the aquaculture farm on a daily basis.</p>

    <footer class="footer" style="left:527px;padding-left:8px;font-size:11px">11</footer>
  </section>

</main>
</body>
</html>
```